Veltrane Management

We need a web design for a new consulting company, with clients all over the world. The company provides management consulting to the travel industry.

Logo files are attached.

Website must look very corporate and be responsive in design.

Management Consulting

```html
<!DOCTYPE html>
<html lang="en">
<head>
<meta charset="utf-8">
<title>Veltrane Management</title>
<link href="https://fonts.googleapis.com/css2?family=Open+Sans:wght@400;600&display=swap" rel="stylesheet">
<style>
:root{
  --page:#f0f0f0;
  --panel:#ffffff;
  --blue:#1a7bbf;
  --green:#5cb85c;
  --green-light:#7fe07f;
  --text:#666666;
  --muted:#777777;
  --rule:#e2e2e2;
}
*{margin:0;padding:0;box-sizing:border-box}
html,body{width:898px;height:1200px;overflow:hidden}
body{background:var(--page);font-family:"Open Sans",Arial,sans-serif;color:var(--text);position:relative}
.brand{position:absolute;left:75px;top:17px;display:flex;align-items:center;gap:9px}
.brand-mark{width:52px;height:52px;border-radius:50%;background:var(--blue)}
.brand-name{color:var(--blue);font-weight:600;line-height:1}
.brand-name .main{display:block;font-size:30px;letter-spacing:.5px}
.brand-name .sub{display:block;font-size:10px;letter-spacing:1.6px;margin-top:3px}
.main-nav{position:absolute;top:35px;right:74px;display:flex;gap:31px;font-size:12px}
.main-nav a{color:var(--muted);text-decoration:none}
.main-nav a.active{color:var(--blue);font-weight:600}
.hero{position:absolute;left:74px;top:87px;width:750px;height:355px;
  background:linear-gradient(90deg,#2f6d72 0%,#556063 30%,#2a2f36 55%,#3d7f86 80%,#1f3b40 100%)}
.hero-arrow{position:absolute;top:158px}
.hero-arrow.prev{left:16px}
.hero-arrow.next{right:16px}
.hero-caption{position:absolute;left:16px;top:265px;width:269px;padding:4px 9px;background:rgba(0,0,0,.6);
  color:var(--green-light);font-size:19.5px;line-height:27px;white-space:nowrap}
.panel{position:absolute;left:74px;top:442px;width:750px;height:650px;background:var(--panel)}
.panel::before{content:"";position:absolute;left:10px;right:10px;top:0;height:14px;
  background:radial-gradient(ellipse at top,rgba(0,0,0,.18),rgba(0,0,0,0) 70%)}
.welcome{position:absolute;left:40px;width:670px;top:28px;text-align:center}
.welcome h1{font-weight:400;font-size:21px;color:var(--blue)}
.welcome p{margin-top:12px;font-size:11.2px;line-height:18.7px}
.btn{display:inline-block;margin-top:15px;padding:4px 8px;background:linear-gradient(#6fcf6f,#4fae4f);
  border-radius:3px;color:#fff;font-size:11px;text-decoration:none}
.rule{position:absolute;left:10px;width:732px;height:1px;background:var(--rule)}
.services{position:absolute;left:10px;top:208px;display:flex;gap:16px}
.service{width:171px;text-align:center}
.service .photo{height:125px}
.service h2{margin-top:8px;font-size:14px;font-weight:600;color:var(--blue);letter-spacing:.2px}
.blog-head{position:absolute;left:10px;top:400px;width:732px;display:flex;justify-content:space-between;align-items:center}
.blog-head h2{font-weight:400;font-size:17px;color:var(--green)}
.post{position:absolute;left:10px;top:442px;width:350px}
.post h3{font-weight:400;font-size:13.5px;color:var(--blue)}
.post time{display:block;font-size:11.5px;color:#555;margin-top:2px}
.post p{margin-top:9px;font-size:10.2px;line-height:18.8px}
.post-icons{display:flex;gap:14px;margin-top:13px}
.post-photo{position:absolute;left:377px;top:445px;width:364px;height:178px;
  background:linear-gradient(160deg,#eef3f7 0%,#a9c1d3 45%,#5f7f98 75%,#f2c45a 100%)}
.footer{position:absolute;left:75px;top:1113px;font-size:10px;color:var(--muted);line-height:23.4px}
.footer a{color:var(--muted);text-decoration:none}
.footer .sep{margin:0 6px}
.social{position:absolute;right:73px;top:1133px;display:flex;gap:5px}
.social span{width:26px;height:26px;border-radius:50%;display:flex;align-items:center;justify-content:center}
.s1{background:#3b5a9a}.s2{background:#1c9be0}.s3{background:#333}.s4{background:var(--green)}
</style>
</head>
<body>
<header>
  <div class="brand">
    <span class="brand-mark"></span>
    <span class="brand-name"><span class="main">VELTRANE</span><span class="sub">STRATEGY MANAGEMENT, INC.</span></span>
  </div>
  <nav class="main-nav">
    <a class="active" href="#">HOME</a><a href="#">ABOUT US</a><a href="#">SERVICES</a><a href="#">BLOG</a><a href="#">CONTACT US</a>
  </nav>
</header>

<section class="hero" role="img" aria-label="Two business travellers smiling on a train, one handing the other a tablet">
  <svg class="hero-arrow prev" width="22" height="40" viewBox="0 0 22 40"><path d="M20 2 L3 20 L20 38" fill="none" stroke="#fff" stroke-width="2"/></svg>
  <svg class="hero-arrow next" width="22" height="40" viewBox="0 0 22 40"><path d="M2 2 L19 20 L2 38" fill="none" stroke="#fff" stroke-width="2"/></svg>
  <div class="hero-caption">Maecenas vitae justo varius<br>imperdiet eros</div>
</section>

<main class="panel">
  <section class="welcome">
    <h1>Welcome to Veltrane</h1>
    <p>Cras id sodales orci. Donec vitae pellentesque ante. Proin auctor dolor vel consequat pharetra. Proin libero felis, iaculis laoreet est faucibus, bibendum efficitur velit. Phasellus gravida urna a ligula gravida feugiat. Nam sed quam tortor. Sed aliquet, turpis id maxi mus fermentum, ex quam vulputate arcu, convallis tristique neque tellus sollicitudin orci.</p>
    <a class="btn" href="#">Read more</a>
  </section>

  <div class="rule" style="top:192px"></div>

  <section class="services">
    <div class="service"><div class="photo" role="img" aria-label="Business travellers with luggage in an airport" style="background:linear-gradient(90deg,#e8ecee,#6d7276 50%,#eceeef)"></div><h2>CORPORATE TRAVEL</h2></div>
    <div class="service"><div class="photo" role="img" aria-label="Sailboats on a deep blue sea" style="background:linear-gradient(#5a9ad6,#8fb4d4 55%,#1d4f92 70%,#123e80)"></div><h2>EVENTS TRAVEL</h2></div>
    <div class="service"><div class="photo" role="img" aria-label="Smiling woman in a winter hat" style="background:linear-gradient(90deg,#8a7c70,#c9b49c 45%,#a8adb2)"></div><h2>LEISURE TRAVEL</h2></div>
    <div class="service"><div class="photo" role="img" aria-label="Woman holding a glowing globe" style="background:radial-gradient(circle at 55% 65%,#2f86c9,#3d4a4c 55%,#1e2122)"></div><h2>RESOURCE TRAVEL</h2></div>
  </section>

  <div class="rule" style="top:373px"></div>

  <div class="blog-head">
    <h2>LATEST BLOG</h2>
    <svg width="13" height="13" viewBox="0 0 13 13"><circle cx="6.5" cy="6.5" r="6.5" fill="#bdbdbd"/><path d="M5 3.5 L8.5 6.5 L5 9.5Z" fill="#fff"/></svg>
  </div>

  <article class="post">
    <h3>Aliquam blandit mattis velit vitae sagittis</h3>
    <time>Oct 8, 2014</time>
    <p>Phasellus dapibus aliquam pharetra. In nunc libero, pulvinar eu ultricies vitae, mollis ut sem. Cras id sodales orci. Donec vitae pellentesque ante. Proin auctor dolor vel consequat pharetra. Proin libero felis, iaculis lao-reet est faucibus, bibendum efficitur velit. Phasellus gravida urna a ligula gravida feugiat. Nam sed quam tortor. Sed aliquet, turpis id maximus fermentum, ex quam vulputate arcu, convallis tristique.</p>
    <div class="post-icons">
      <svg width="12" height="10" viewBox="0 0 12 10"><path d="M0 2h3l5 6h3M0 8h3l5-6h3M9 0l2 2-2 2M9 6l2 2-2 2" fill="none" stroke="#888" stroke-width="1.2"/></svg>
      <svg width="11" height="10" viewBox="0 0 11 10"><path d="M0 0h11v7H4L1 10V7H0Z" fill="#888"/></svg>
    </div>
  </article>
  <div class="post-photo" role="img" aria-label="Curving highway overpass in sunlight"></div>
</main>

<footer class="footer">
  <div><a href="#">HOME</a><span class="sep">/</span><a href="#">ABOUT US</a><span class="sep">/</span><a href="#">SERVICES</a><span class="sep">/</span><a href="#">BLOG</a><span class="sep">/</span><a href="#">CONTACT US</a></div>
  <div>Copyright © 2014 Veltrane. All rights reserved</div>
  <div>Call : 456 321 7702 / E-mail : info@veltrane.com</div>
</footer>
<div class="social">
  <span class="s1"></span><span class="s2"></span><span class="s3"></span>
  <span class="s4"><svg width="14" height="10" viewBox="0 0 14 10"><rect x=".5" y=".5" width="13" height="9" fill="#fff"/><path d="M.5 .5 L7 5.5 L13.5 .5" fill="none" stroke="#5cb85c"/></svg></span>
</div>
</body>
</html>
```